Marketing Postcard Design for a Medical Supply Company

We are sending a marketing postcard to healthcare facilities within our state. We are in need of a design for a 6"x9" postcard, front and back with our logo, website www.curaloft.shop, phone number 808-413-2759, and 12 products. The products are face shields, nitrile gloves, vinyl gloves, isolation gowns, gallon hand sanitizer, black KN95's, white KN95's, 4320 R77, 4310 R77, biohazard bags, Purivane wipes, and Kol spray. All of these items can be found on our website at curaloft.shop. Please include a promo code, 10OFF for 10% Off. The design should be clean, professional, and appeal to a healthcare or medical audience.

```html
<!DOCTYPE html>
<html lang="en">
<head>
<meta charset="utf-8">
<title>Curaloft Medical Supply – Postcard Front and Back</title>
<link href="https://fonts.googleapis.com/css2?family=Montserrat:wght@300;400;600;700;800&display=swap" rel="stylesheet">
<style>
  :root {
    --page-bg: #e1e3e0;
    --white: #ffffff;
    --sky-light: #eef5fa;
    --sky-mid: #d6e7f3;
    --green-deep: #1c6a37;
    --green-forest: #1b5e30;
    --green-bright: #18963f;
    --green-panel: #1f8b3d;
    --green-badge: #4eaa3a;
    --brand-green: #1b8a3a;
  }
  * { margin: 0; padding: 0; box-sizing: border-box; }
  html, body {
    width: 986px; height: 1200px; overflow: hidden;
    background: var(--page-bg);
    font-family: "Montserrat", sans-serif;
  }
  .postcard {
    position: absolute; left: 116px;
    width: 760px; height: 507px;
    background: var(--white);
    overflow: hidden;
  }
  .postcard--front { top: 75px; }
  .postcard--back { top: 647px; }
  .card-art { position: absolute; inset: 0; width: 760px; height: 507px; }

  .brand {
    position: absolute; width: 240px; text-align: center;
    color: var(--brand-green); font-weight: 700; line-height: 1;
  }
  .brand__name { display: block; font-size: 31px; letter-spacing: -0.5px; }
  .brand__tag { display: block; font-size: 10px; letter-spacing: 2.6px; margin-top: 6px; }
  .postcard--front .brand { left: -4px; top: 52px; }
  .postcard--back .brand { left: 2px; top: 58px; }

  .section-title {
    position: absolute; left: 35px; top: 157px;
    color: var(--white); font-size: 17.5px; font-weight: 400; letter-spacing: 0.3px;
  }
  .section-title strong { font-weight: 700; }

  .product {
    position: absolute; height: 54px;
    display: flex; align-items: center;
    color: var(--white); font-size: 12.5px; font-weight: 600;
    letter-spacing: 0.5px; line-height: 18px; text-transform: uppercase;
  }
  .product--left { left: 28px; gap: 10px; }
  .product--right { left: 207px; gap: 20px; }
  .postcard--back .product--left { gap: 16px; }
  .postcard--back .product--right { gap: 15px; }
  .product__icon {
    width: 54px; height: 54px; flex: none;
    border-radius: 50%; border: 1.5px dotted var(--white);
    display: flex; align-items: center; justify-content: center;
  }
  .product__art {
    width: 43px; height: 43px; border-radius: 50%;
    background: radial-gradient(circle at 50% 45%, #cfe9f3 0 40%, var(--white) 42%);
  }

  .contact {
    position: absolute; left: 35px;
    display: flex; align-items: center;
    color: var(--white);
  }
  .postcard--front .contact { top: 450px; }
  .postcard--back .contact { top: 443px; }
  .contact__icon { width: 30px; height: 30px; flex: none; }
  .contact__phone { font-size: 20.5px; font-weight: 300; margin-left: 16px; letter-spacing: 0.3px; }
  .contact__globe { width: 22px; height: 22px; margin-left: 20px; flex: none; }
  .contact__web { font-size: 13px; font-weight: 400; margin-left: 10px; }

  .promo {
    position: absolute; left: 442px; top: 357px;
    width: 142px; height: 142px;
  }
  .promo__text {
    position: absolute; inset: 0; color: var(--white); text-align: center;
  }
  .promo__code { position: absolute; top: 38px; left: 0; right: 0; font-size: 16px; font-weight: 700; }
  .promo__value { position: absolute; top: 54px; left: 0; right: 0; font-size: 46px; font-weight: 800; letter-spacing: -1px; }
  .promo__off { position: absolute; top: 100px; right: 42px; font-size: 12px; font-weight: 400; }
</style>
</head>
<body>

<!-- Front -->
<section class="postcard postcard--front">
  <svg class="card-art" viewBox="0 0 760 507" aria-hidden="false">
    <defs>
      <linearGradient id="skyFront" x1="0" y1="0" x2="1" y2="0">
        <stop offset="0" stop-color="var(--sky-light)"/>
        <stop offset="1" stop-color="var(--sky-mid)"/>
      </linearGradient>
      <linearGradient id="cleanroomTones" x1="0" y1="0" x2="1" y2="1">
        <stop offset="0" stop-color="#dfe8ec"/>
        <stop offset="0.5" stop-color="#a9c4c6"/>
        <stop offset="1" stop-color="#7ea7a5"/>
      </linearGradient>
    </defs>
    <rect class="sky-band" x="0" y="0" width="760" height="143" fill="url(#skyFront)"/>
    <rect class="product-panel" x="0" y="143" width="520" height="289" fill="var(--green-deep)"/>
    <rect class="contact-bar" x="0" y="443" width="540" height="43" fill="var(--green-bright)"/>
    <path class="arc-band" d="M655 0 C470 60 385 190 395 300 C402 390 430 460 452 507 L760 507 L760 0 Z" fill="var(--green-bright)"/>
    <path class="arc-line" d="M646 0 C461 62 377 190 387 300 C394 390 420 460 442 507" fill="none" stroke="var(--white)" stroke-width="3"/>
    <g role="img" aria-label="Photo of workers in teal cleanroom suits operating packaging equipment in a medical supply facility">
      <path d="M718 0 C520 55 412 190 420 300 C426 390 455 460 480 507 L760 507 L760 0 Z" fill="url(#cleanroomTones)"/>
    </g>
    <path class="corner-top" d="M700 0 L760 0 L760 68 C745 40 725 18 700 0 Z" fill="var(--white)"/>
    <path class="corner-bottom" d="M680 507 C715 480 742 455 760 425 L760 507 Z" fill="var(--white)"/>
  </svg>

  <div class="brand">
    <span class="brand__name">CURALOFT</span>
    <span class="brand__tag">MEDICAL SUPPLY</span>
  </div>

  <h2 class="section-title"><strong>OUR BEST</strong> PRODUCTS</h2>

  <div class="product product--left" style="top:194px">
    <div class="product__icon"><div class="product__art" role="img" aria-label="Face shield icon"></div></div>
    <span>Face Shields</span>
  </div>
  <div class="product product--right" style="top:194px">
    <div class="product__icon"><div class="product__art" role="img" aria-label="Nitrile glove icon"></div></div>
    <span>Nitrile Gloves</span>
  </div>
  <div class="product product--left" style="top:272px">
    <div class="product__icon"><div class="product__art" role="img" aria-label="Vinyl glove icon"></div></div>
    <span>Vinyl Gloves</span>
  </div>
  <div class="product product--right" style="top:272px">
    <div class="product__icon"><div class="product__art" role="img" aria-label="Isolation gown icon"></div></div>
    <span>Isolation<br>Gowns</span>
  </div>
  <div class="product product--left" style="top:354px">
    <div class="product__icon"><div class="product__art" role="img" aria-label="Hand sanitizer gallon icon"></div></div>
    <span>Gallon Hand<br>Sanitizer</span>
  </div>
  <div class="product product--right" style="top:354px">
    <div class="product__icon"><div class="product__art" role="img" aria-label="Black KN95 mask icon"></div></div>
    <span>Black KN95's</span>
  </div>

  <div class="contact">
    <svg class="contact__icon" viewBox="0 0 30 30" aria-hidden="true">
      <path d="M6 4 L10 3 L13 10 L10 12 C11 16 14 19 18 20 L20 17 L27 20 L26 24 C25 27 22 28 19 27 C11 24 6 19 3 11 C2 8 3 5 6 4 Z" fill="var(--white)"/>
      <path d="M17 8 A6 6 0 0 1 22 13 M18 4 A10 10 0 0 1 26 12 M19 0.5 A14 14 0 0 1 29.5 11" fill="none" stroke="var(--white)" stroke-width="1.8" stroke-linecap="round"/>
    </svg>
    <span class="contact__phone">808-413-2759</span>
    <svg class="contact__globe" viewBox="0 0 22 22" aria-hidden="true">
      <g fill="none" stroke="var(--white)" stroke-width="1.8">
        <circle cx="11" cy="11" r="9.5"/>
        <ellipse cx="11" cy="11" rx="4.2" ry="9.5"/>
        <line x1="1.5" y1="11" x2="20.5" y2="11"/>
        <path d="M3 6 H19 M3 16 H19"/>
      </g>
    </svg>
    <span class="contact__web">www.curaloft.shop</span>
  </div>

  <div class="promo">
    <svg viewBox="0 0 142 142" width="142" height="142" aria-hidden="true">
      <circle cx="71" cy="71" r="62" fill="var(--green-badge)"/>
      <circle cx="71" cy="71" r="66" fill="none" stroke="var(--green-badge)" stroke-width="8" stroke-dasharray="4.3 4.3"/>
      <circle cx="71" cy="71" r="57" fill="var(--green-forest)"/>
    </svg>
    <div class="promo__text">
      <span class="promo__code">10OFF for</span>
      <span class="promo__value">10%</span>
      <span class="promo__off">Off</span>
    </div>
  </div>
</section>

<!-- Back -->
<section class="postcard postcard--back">
  <svg class="card-art" viewBox="0 0 760 507">
    <defs>
      <linearGradient id="skyBack" x1="0" y1="0" x2="1" y2="0">
        <stop offset="0" stop-color="var(--sky-light)"/>
        <stop offset="1" stop-color="var(--sky-mid)"/>
      </linearGradient>
      <linearGradient id="panelBack" x1="0" y1="0" x2="1" y2="0">
        <stop offset="0" stop-color="#238f3f"/>
        <stop offset="1" stop-color="#1c7a37"/>
      </linearGradient>
      <linearGradient id="workerTones" x1="0" y1="0" x2="1" y2="1">
        <stop offset="0" stop-color="#c9ccd1"/>
        <stop offset="0.55" stop-color="#dfe3e8"/>
        <stop offset="1" stop-color="#f1f3f6"/>
      </linearGradient>
    </defs>
    <rect class="sky-band" x="0" y="0" width="760" height="152" fill="url(#skyBack)"/>
    <rect class="product-panel" x="0" y="152" width="560" height="279" fill="url(#panelBack)"/>
    <rect class="contact-bar" x="0" y="437" width="600" height="44" fill="var(--green-forest)"/>
    <path class="arc-line" d="M472 0 C412 120 392 220 422 300 C452 390 512 460 582 507" fill="none" stroke="var(--white)" stroke-width="3"/>
    <path class="arc-band" d="M480 0 C420 120 400 220 430 300 C460 390 520 460 590 507 L760 507 L760 0 Z" fill="var(--green-forest)"/>
    <g role="img" aria-label="Photo of a healthcare worker in a face shield, hair net, respirator mask and white gown pulling on blue gloves">
      <path d="M502 0 C442 120 424 220 452 300 C480 385 535 460 603 507 L760 507 L760 0 Z" fill="url(#workerTones)"/>
    </g>
    <path class="arc-corner" d="M622 0 C680 25 730 75 760 137 L760 100 C730 55 690 20 660 0 Z" fill="var(--green-forest)"/>
    <path class="corner-top" d="M660 0 L760 0 L760 100 C730 55 690 20 660 0 Z" fill="var(--white)"/>
  </svg>

  <div class="brand">
    <span class="brand__name">CURALOFT</span>
    <span class="brand__tag">MEDICAL SUPPLY</span>
  </div>

  <div class="product product--left" style="top:187px">
    <div class="product__icon"><div class="product__art" role="img" aria-label="White KN95 mask icon"></div></div>
    <span>White KN95's</span>
  </div>
  <div class="product product--right" style="top:187px">
    <div class="product__icon"><div class="product__art" role="img" aria-label="Biohazard bag icon"></div></div>
    <span>Biohazard Bags</span>
  </div>
  <div class="product product--left" style="top:266px">
    <div class="product__icon"><div class="product__art" role="img" aria-label="Respirator mask icon"></div></div>
    <span>4320 R77</span>
  </div>
  <div class="product product--right" style="top:266px">
    <div class="product__icon"><div class="product__art" role="img" aria-label="Disinfecting wipes canister icon"></div></div>
    <span>Purivane<br>Wipes</span>
  </div>
  <div class="product product--left" style="top:348px">
    <div class="product__icon"><div class="product__art" role="img" aria-label="Surgical mask icon"></div></div>
    <span>4310 R77</span>
  </div>
  <div class="product product--right" style="top:343px">
    <div class="product__icon"><div class="product__art" role="img" aria-label="Spray bottle icon"></div></div>
    <span>Kol Spray</span>
  </div>

  <div class="contact">
    <svg class="contact__icon" viewBox="0 0 30 30" aria-hidden="true">
      <path d="M6 4 L10 3 L13 10 L10 12 C11 16 14 19 18 20 L20 17 L27 20 L26 24 C25 27 22 28 19 27 C11 24 6 19 3 11 C2 8 3 5 6 4 Z" fill="var(--white)"/>
      <path d="M17 8 A6 6 0 0 1 22 13 M18 4 A10 10 0 0 1 26 12 M19 0.5 A14 14 0 0 1 29.5 11" fill="none" stroke="var(--white)" stroke-width="1.8" stroke-linecap="round"/>
    </svg>
    <span class="contact__phone">808-413-2759</span>
    <svg class="contact__globe" viewBox="0 0 22 22" aria-hidden="true">
      <g fill="none" stroke="var(--white)" stroke-width="1.8">
        <circle cx="11" cy="11" r="9.5"/>
        <ellipse cx="11" cy="11" rx="4.2" ry="9.5"/>
        <line x1="1.5" y1="11" x2="20.5" y2="11"/>
        <path d="M3 6 H19 M3 16 H19"/>
      </g>
    </svg>
    <span class="contact__web">www.curaloft.shop</span>
  </div>
</section>

</body>
</html>
```